German Webagency needs fresh modern Design

Our website is 4 years old. We need an fresh modern website. All pics we used before are from customers or handmade by us. the new website should be clear with nice handling. please dont copy something from template websites. it would be great if you can surprise us with something great. its our first project here. don´t worry if i make a mistake in responding or briefing. after 20 years you can´t see the works of your own "designer" so we hope for help :-)
our existing site: www.tovankreativ.de
Target Market(s)
small and middle sized companys in germany
Number of Pages Required
4 page
Font styles to use
Colors
Designer to choose colors to be used in the design.
Requirements
Must have
- Responsive (sure we code it)
- Modern and big Font ..Headlines and Slider
- innovative..if you know something new..feel free to show
Nice to have
- the site with our works/refences should look great and later easy to handle when we code it or use wp.
- we like black and grey but if you have better ideas also feel free
Should not have
- a cup of coffe..laptop.. a pencil a handwritten font
- dont copy and modify templates from know websites..bad style

```html
<!DOCTYPE html>
<html lang="de">
<head>
<meta charset="utf-8">
<title>tovankreativ.de</title>
<link href="https://fonts.googleapis.com/css2?family=Montserrat:wght@700;800&display=swap" rel="stylesheet">
<style>
  :root {
    --sky-top: #a4c7e4;
    --sky-bottom: #b1cde4;
    --white: #ffffff;
    --brand-blue: #3784c2;
    --rock-dark: #161c22;
    --rock-mid: #2f3a44;
    --rock-soft: #6f8294;
    --text-dark: #1b1d21;
  }
  * { margin: 0; padding: 0; box-sizing: border-box; }
  html, body { width: 1200px; height: 750px; overflow: hidden; }
  body {
    font-family: "Montserrat", Arial, sans-serif;
    background: linear-gradient(180deg, var(--sky-top), var(--sky-bottom));
    position: relative;
    color: var(--white);
  }
  .hero-visual {
    position: absolute; left: 0; top: 0; width: 390px; height: 750px;
    background: linear-gradient(90deg, var(--rock-dark) 0%, var(--rock-mid) 55%, var(--rock-soft) 85%, var(--sky-top) 100%);
  }
  .logo-box {
    position: absolute; left: 429px; top: 0; width: 210px; height: 94px;
    background: var(--white); border-radius: 0 0 13px 13px;
    display: flex; align-items: center; justify-content: center; gap: 8px;
  }
  .logo-dot { width: 10px; height: 10px; border-radius: 50%; background: var(--brand-blue); }
  .logo-name { font-weight: 800; font-size: 16px; color: var(--text-dark); letter-spacing: 0.01em; }
  .main-nav {
    position: absolute; left: 689px; top: 38px;
    display: flex; gap: 24px; font-weight: 700; font-size: 14px;
  }
  .main-nav a { color: var(--white); text-decoration: none; }
  .headline {
    position: absolute; left: 429px; top: 338px;
    font-weight: 800; font-size: 56px; line-height: 69px;
    letter-spacing: 0.125em; text-transform: uppercase; white-space: nowrap;
  }
  .actions { position: absolute; left: 428px; top: 589px; display: flex; gap: 25px; }
  .btn-contact {
    width: 228px; height: 54px; border-radius: 27px; background: var(--brand-blue);
    color: var(--white); font-weight: 800; font-size: 20px; letter-spacing: 0.1em;
    display: flex; align-items: center; justify-content: center; text-decoration: none;
  }
  .social-link {
    width: 54px; height: 54px; border-radius: 50%; background: var(--white);
    display: flex; align-items: center; justify-content: center;
  }
  .share-icon { width: 20px; height: 20px; }
</style>
</head>
<body>
  <div class="hero-visual" role="img" aria-label="Foto eines schneebedeckten Felsgrats mit blauem Fluss"></div>

  <div class="logo-box">
    <span class="logo-dot"></span>
    <span class="logo-name">tovankreativ.de</span>
  </div>

  <nav class="main-nav">
    <a href="#">Über uns</a>
    <a href="#">Services</a>
    <a href="#">Referenzen</a>
    <a href="#">Kontakt</a>
  </nav>

  <h1 class="headline">Ideen &amp; Visionen<br>gemeinsam<br>verwirklichen</h1>

  <div class="actions">
    <a class="btn-contact" href="#">KONTAKT</a>
    <a class="social-link" href="#" aria-label="Soziales Netzwerk 1">
      <svg class="share-icon" viewBox="0 0 20 20" fill="var(--brand-blue)" stroke="var(--brand-blue)" stroke-width="1.8">
        <line x1="5" y1="10" x2="15" y2="4"/><line x1="5" y1="10" x2="15" y2="16"/>
        <circle cx="5" cy="10" r="3" stroke="none"/><circle cx="15" cy="4" r="3" stroke="none"/><circle cx="15" cy="16" r="3" stroke="none"/>
      </svg>
    </a>
    <a class="social-link" href="#" aria-label="Soziales Netzwerk 2">
      <svg class="share-icon" viewBox="0 0 20 20" fill="var(--brand-blue)" stroke="var(--brand-blue)" stroke-width="1.8">
        <line x1="5" y1="10" x2="15" y2="4"/><line x1="5" y1="10" x2="15" y2="16"/>
        <circle cx="5" cy="10" r="3" stroke="none"/><circle cx="15" cy="4" r="3" stroke="none"/><circle cx="15" cy="16" r="3" stroke="none"/>
      </svg>
    </a>
    <a class="social-link" href="#" aria-label="Soziales Netzwerk 3">
      <svg class="share-icon" viewBox="0 0 20 20" fill="var(--brand-blue)" stroke="var(--brand-blue)" stroke-width="1.8">
        <line x1="5" y1="10" x2="15" y2="4"/><line x1="5" y1="10" x2="15" y2="16"/>
        <circle cx="5" cy="10" r="3" stroke="none"/><circle cx="15" cy="4" r="3" stroke="none"/><circle cx="15" cy="16" r="3" stroke="none"/>
      </svg>
    </a>
  </div>
</body>
</html>
```